Waschkarten-Design für Tankstelle gesucht
Zielgruppe
Unsere Tankstelle hat in eine neue Waschanlage investiert. Die Alten Waschkarten gefallen nicht mehr, und sind auch mit der Programmstruktur nicht mehr kompatibel. Siehe Anhang.
Waschkunden in der Portalwaschanlage jeglichen Alters und Geschlechts.
Aufgabenstellung
Wertigkeit der einzelnen Waschprogramme muss erkennbar sein. Beschriftung z. B. Mehrfachwäschen 3er 5er 10er bzw. Wertkarten der Preis soll veränderbar sein, so das die Karten jederzeit angepasst werden können. Auch sollte der Programm-Name von uns selbst geändert werden können. Die Einschiebe Richtung muss klar erkennbar sein.
Das Design muss im Check-Kartenformat sein. Achtung abgerundete Ecken mit ca. r=2 mm
Anbei ein Bild von unserer Neuen Waschanlage

```html
<!DOCTYPE html>
<html lang="de">
<head>
<meta charset="utf-8">
<title>Waschkarten – Tankstelle Lindner</title>
<link rel="stylesheet" href="https://fonts.googleapis.com/css2?family=Ubuntu:wght@400;500;700&display=swap">
<style>
  :root {
    --frame: #0b4a5e;
    --paper: #ffffff;
    --ink-light: #ffffff;
    --ink-dark: #141414;
    --express-a: #6a6556;
    --express-b: #4a463c;
    --express-photo-a: #7a8088;
    --express-photo-b: #3f4246;
    --top-a: #5b7fa4;
    --top-b: #3c5673;
    --top-photo-a: #6f8296;
    --top-photo-b: #353d47;
    --premium-a: #857a3e;
    --premium-b: #5b532c;
    --premium-photo-a: #7f7a5c;
    --premium-photo-b: #3e3b2c;
  }
  * { box-sizing: border-box; margin: 0; padding: 0; }
  html, body { width: 1200px; height: 1200px; overflow: hidden; }
  body {
    background: var(--paper);
    font-family: "Ubuntu", sans-serif;
    position: relative;
  }
  .frame {
    position: absolute; inset: 0;
    border: 6px solid var(--frame);
  }
  .card {
    position: absolute;
    left: 360px;
    width: 480px;
    height: 304px;
    overflow: hidden;
  }
  .card--express { top: 132px; }
  .card--top { top: 448px; }
  .card--premium { top: 764px; }

  .card__panel {
    position: absolute; left: 0; top: 0;
    width: 166px; height: 100%;
  }
  .card__photo {
    position: absolute; left: 166px; top: 0;
    width: 314px; height: 100%;
  }
  .card--express .card__panel { background: radial-gradient(circle at 40% 40%, var(--express-a), var(--express-b)); }
  .card--express .card__photo { background: linear-gradient(180deg, var(--express-photo-a), var(--express-photo-b)); }
  .card--top .card__panel { background: radial-gradient(circle at 30% 50%, var(--top-a), var(--top-b)); }
  .card--top .card__photo { background: linear-gradient(180deg, var(--top-photo-a), var(--top-photo-b)); }
  .card--premium .card__panel { background: radial-gradient(circle at 30% 70%, var(--premium-a), var(--premium-b)); }
  .card--premium .card__photo { background: linear-gradient(180deg, var(--premium-photo-a), var(--premium-photo-b)); }

  .card__arrow { position: absolute; left: 0; top: 0; }

  .card__title {
    position: absolute; left: 12px; top: 26px;
    font-weight: 700; font-size: 68px; line-height: 1;
    color: var(--ink-light);
    letter-spacing: 0.5px;
    text-shadow: 0 4px 14px rgba(0,0,0,0.45);
  }
  .card--top .card__title { left: 17px; }
  .card__program {
    position: absolute; left: 14px; top: 98px;
    font-size: 29px; line-height: 34px;
    color: var(--ink-light);
    text-shadow: 0 2px 6px rgba(0,0,0,0.3);
  }
  .card__price {
    position: absolute; right: 42px; top: 185px;
    font-size: 59px; line-height: 1;
    color: var(--ink-light);
    text-shadow: 0 2px 8px rgba(0,0,0,0.35);
  }
  .card__brand {
    position: absolute; left: 14px; top: 214px;
    width: 140px;
    display: flex; align-items: center; gap: 7px;
    font-weight: 500; font-size: 22px;
    color: var(--ink-dark);
  }
  .card__brand-dot {
    width: 12px; height: 12px; border-radius: 50%;
    background: var(--ink-dark);
    flex: none;
  }
</style>
</head>
<body>
  <div class="frame"></div>

  <section class="card card--express">
    <div class="card__panel"></div>
    <div class="card__photo" role="img" aria-label="Foto der Portalwaschanlage mit Bürsten vor bewölktem Himmel"></div>
    <svg class="card__arrow" width="480" height="304" aria-hidden="true">
      <polygon points="240,197 359,197 359,164 466,227 359,290 359,257 240,257" fill="rgba(255,255,255,0.55)"/>
    </svg>
    <h2 class="card__title">EXPRESS</h2>
    <p class="card__program">Waschen und Trocknen</p>
    <p class="card__price">€ 5,95</p>
    <div class="card__brand"><span class="card__brand-dot"></span>Lindner</div>
  </section>

  <section class="card card--top">
    <div class="card__panel"></div>
    <div class="card__photo" role="img" aria-label="Foto der Portalwaschanlage mit Bürsten vor bewölktem Himmel"></div>
    <svg class="card__arrow" width="480" height="304" aria-hidden="true">
      <polygon points="240,197 359,197 359,164 466,227 359,290 359,257 240,257" fill="rgba(255,255,255,0.55)"/>
    </svg>
    <h2 class="card__title">TOP</h2>
    <p class="card__program">Wachs und Unterboden</p>
    <p class="card__price">€ 12,95</p>
    <div class="card__brand"><span class="card__brand-dot"></span>Lindner</div>
  </section>

  <section class="card card--premium">
    <div class="card__panel"></div>
    <div class="card__photo" role="img" aria-label="Foto der Portalwaschanlage mit Bürsten vor bewölktem Himmel"></div>
    <svg class="card__arrow" width="480" height="304" aria-hidden="true">
      <polygon points="240,197 359,197 359,164 466,227 359,290 359,257 240,257" fill="rgba(255,255,255,0.55)"/>
    </svg>
    <h2 class="card__title">PREMIUM</h2>
    <p class="card__program">Politurprogramm mit<br>Unterbodenwäsche</p>
    <p class="card__price">€ 16,95</p>
    <div class="card__brand"><span class="card__brand-dot"></span>Lindner</div>
  </section>
</body>
</html>
```